Property Developer Business card design

we need a business card design + printing for a new Property developer company based in melbourne.
We are a group of investors investing in a property developer business. We have more projects involved in residential property as opposed to commercial property but we are involved in both market. we also provide consulting services with overseas investors willing to invest in the australian property market.
Updates
I have uploaded the logo. I'm not very convince with the colors of my logo... any suggestion please?.
Thanks guys!
Target Market(s)
property investors or person willing to purchase investment property
Industry/Entity Type
Residential
Contact Information for Business Card
Tallgrove Holdings Australia Pty Ltd
Look and feel
Each slider illustrates characteristics of the customer's brand and the style your logo design should communicate.

```html
<!DOCTYPE html>
<html lang="en">
<head>
<meta charset="utf-8">
<title>Tallgrove Holdings – Business Card</title>
<link href="https://fonts.googleapis.com/css2?family=Open+Sans:wght@400;600;700&display=swap" rel="stylesheet">
<style>
  :root {
    --stage: #1f1f21;
    --card-white: #f4f5f7;
    --navy: #1d3a86;
    --royal: #3f6fd0;
    --sky: #6a9be6;
    --cyan: #35c7e0;
    --ocean: #2a7ac4;
    --red: #e0262c;
    --brand-blue: #2fa9de;
    --ink-white: #ffffff;
  }
  * { margin: 0; padding: 0; box-sizing: border-box; }
  html, body { width: 1200px; height: 900px; overflow: hidden; }
  body {
    background: var(--stage);
    font-family: "Open Sans", Arial, sans-serif;
    position: relative;
  }
  .card {
    position: absolute;
    width: 584px;
    height: 335px;
    border-radius: 28px;
    overflow: hidden;
  }
  .card--back {
    left: 316px; top: 87px;
    background: radial-gradient(ellipse 60% 70% at 55% 35%, var(--sky) 0%, var(--royal) 50%, var(--navy) 100%);
  }
  .card--front {
    left: 316px; top: 475px;
    background: radial-gradient(ellipse at 50% 30%, #ffffff 0%, var(--card-white) 60%, #dfe2e7 100%);
  }
  .brand-name {
    position: absolute;
    font-weight: 600;
    white-space: nowrap;
  }
  .card--back .brand-name {
    right: 22px; bottom: 20px;
    font-size: 24px;
    color: var(--ink-white);
  }
  .card--front .brand-name {
    left: 0; right: 0; top: 108px;
    text-align: center;
    font-size: 34px;
    color: var(--brand-blue);
  }
  .bands { position: absolute; left: 0; top: 0; width: 584px; height: 335px; }
  .person {
    position: absolute;
    left: 420px; top: 206px; width: 150px;
    text-align: center;
    color: var(--ink-white);
  }
  .person__name { font-size: 20px; font-weight: 700; line-height: 24px; }
  .person__role { font-size: 11px; font-weight: 600; line-height: 14px; }
  .company-address {
    position: absolute;
    right: 351px; top: 260px;
    text-align: right;
    color: var(--ink-white);
    font-size: 11.5px;
    line-height: 18px;
  }
  .company-address__name { font-weight: 700; }
  .divider {
    position: absolute;
    left: 256px; top: 255px;
    width: 1px; height: 65px;
    background: rgba(255,255,255,0.5);
  }
  .contact-list {
    position: absolute;
    left: 278px; top: 251px;
    list-style: none;
    color: var(--ink-white);
    font-size: 11.5px;
    line-height: 17.5px;
  }
  .contact-list li { display: flex; align-items: center; gap: 5px; }
  .contact-list svg { width: 11px; height: 11px; flex: none; }
</style>
</head>
<body>

<section class="card card--back" aria-label="Card back">
  <span class="brand-name">Tallgrove Holdings</span>
</section>

<section class="card card--front" aria-label="Card front">
  <span class="brand-name">Tallgrove Holdings</span>

  <svg class="bands" viewBox="0 0 584 335" aria-hidden="true">
    <defs>
      <linearGradient id="ocean-band" x1="0" y1="0" x2="0" y2="1">
        <stop offset="0" stop-color="#3fd3e6"/>
        <stop offset="0.6" stop-color="#2f8fd0"/>
        <stop offset="1" stop-color="#2a63b8"/>
      </linearGradient>
      <linearGradient id="red-band" x1="0" y1="0" x2="0" y2="1">
        <stop offset="0" stop-color="#ef3a3f"/>
        <stop offset="1" stop-color="#c81d22"/>
      </linearGradient>
    </defs>
    <polygon points="0,197 584,197 584,257 417,257 350,205 0,205" fill="url(#red-band)"/>
    <polygon points="0,210 346,210 410,262 584,262 584,335 0,335" fill="url(#ocean-band)"/>
  </svg>

  <div class="person">
    <p class="person__name">Ravi Mendes</p>
    <p class="person__role">Managing Director</p>
  </div>

  <address class="company-address" style="font-style:normal">
    <p class="company-address__name">Tallgrove Holdings Australia Pty Ltd</p>
    <p>14 Wattlebird Lane</p>
    <p>Fernhill VIC 3030</p>
  </address>

  <div class="divider"></div>

  <ul class="contact-list">
    <li>
      <svg viewBox="0 0 12 12"><rect x="3" y="0.5" width="6" height="11" rx="1.2" fill="none" stroke="#fff" stroke-width="1.2"/><rect x="4.5" y="2" width="3" height="5" fill="#fff"/></svg>
      <span>0400 218 563</span>
    </li>
    <li>
      <svg viewBox="0 0 12 12"><path d="M3 1 L5 3.5 L4 5 Q5.5 7.5 7.5 8.5 L9 7.5 L11 9.5 L9.5 11 Q4 10 1.5 3 Z" fill="#fff"/></svg>
      <span>+61 3 9000 5512</span>
    </li>
    <li>
      <svg viewBox="0 0 12 12"><rect x="0.8" y="2.5" width="10.4" height="7" fill="none" stroke="#fff" stroke-width="1.1"/><path d="M1 3 L6 7 L11 3" fill="none" stroke="#fff" stroke-width="1.1"/></svg>
      <span>ravi.mendes@tallgroveholdings.com.au</span>
    </li>
    <li>
      <svg viewBox="0 0 12 12"><circle cx="6" cy="6" r="5" fill="none" stroke="#fff" stroke-width="1.1"/><ellipse cx="6" cy="6" rx="2.2" ry="5" fill="none" stroke="#fff" stroke-width="1"/><line x1="1" y1="6" x2="11" y2="6" stroke="#fff" stroke-width="1"/></svg>
      <span>www.tallgroveholdings.com.au</span>
    </li>
  </ul>
</section>

</body>
</html>
```